Personal Trainer website design

We are working with a personal trainer to design a website. They offer their primary services: Diet Coaching, In-Person Coaching (workouts), and Remote Coaching.
Some sites we like: https://www.marenkoltby.com, https://tavilobrenn.com/en-us, https://corevandel.co.uk
Thank you for taking the time to consider designing a website for us. We are web developers based in Stockton, CA USA. Most of our projects go through the same process. Understanding this process may help you win a project with us. We custom-code all of our websites in-house. We don’t have any requirements as to what tools you use for your design, but ask that you follow these guidelines.
IMAGES:
We ask that if you use any images, or icons in the design, have a link to the asset, so we can purchase the image/icon. Most of the designs we submit do not have the customer’s images on them unless they have some great images. Be creative; show us the feeling that you are trying to portray with your image choices. Use any royalty-free site you choose. We subscribe to Quillex and mostly use their images, but are ok to purchase images outside of Quillex.
FONTS:
We ask that you identify the fonts you’re using in the design. This can be done in a message if you want. We typically use Brimora Fonts and Quillex Fonts.
CONTENT:
We're always open to different content and ideas. Often, we submit designs with stock images so that the client can see our vision. We typically go back and take pictures after the website launch to use their images with our vision. Lorem Ipsum is fine for paragraphs, but we ask that you make the Headers with correct English. We want to be able to show the vision and identify the sections of the website.
INSPIRATION:
We try and add a couple of links in the brief of some websites that we like to help you get started in your design.
REVISIONS:
We do not often ask for revisions of the designs unless we see something in the design that may not appeal to the client. If there are slight changes that we want to make, we simply do that in the development process.
FEEDBACK:
We rarely give feedback on designs during the design process. We are working on many website projects and do not have the time to give feedback. We usually respond if your request is well thought out and asks specific questions, but a note asking “feedback, please” usually goes unanswered.
1 page

```html
<!DOCTYPE html>
<html lang="en">
<head>
<meta charset="utf-8">
<title>Kelvora – Personal Training</title>
<link href="https://fonts.googleapis.com/css2?family=Epilogue:wght@500;600;700&family=Poppins:wght@400;500;600&display=swap" rel="stylesheet">
<style>
:root{
  --green:#8c9b1d;
  --green-dark:#6f7c12;
  --ink:#1d1d1d;
  --dark:#222322;
  --muted:#8a8a8a;
  --line:#e6e6e6;
  --white:#fff;
}
*{box-sizing:border-box;margin:0;padding:0}
html,body{width:1200px;height:4304px;overflow:hidden}
body{position:relative;background:var(--white);font-family:"Poppins",sans-serif;color:var(--ink)}
.abs{position:absolute}
h1,h2,h3{font-family:"Epilogue",sans-serif}
.btn{position:absolute;display:flex;align-items:center;justify-content:center;background:var(--green);color:#fff;border-radius:30px;font-family:"Epilogue",sans-serif;font-weight:700;text-transform:uppercase;font-size:12px;letter-spacing:.3px}
.fill{position:absolute}

/* nav */
.nav{top:0;left:0;width:1200px;height:79px}
.brand{position:absolute;font-family:"Epilogue",sans-serif;font-weight:700;font-size:28px;color:var(--ink);display:flex;align-items:center;gap:10px;letter-spacing:.5px}
.brand i{display:block;width:18px;height:18px;border-radius:50%;background:var(--green)}
.nav-links{position:absolute;left:393px;top:32px;display:flex;gap:26px;font-family:"Epilogue",sans-serif;font-weight:600;font-size:14px}
.login{left:880px;top:20px;width:177px;height:44px;text-transform:none;font-size:14px;font-weight:600;gap:10px}

/* hero */
.hero{top:79px;left:0;width:1200px;height:610px;background:linear-gradient(100deg,#0b0f16 0%,#151c26 45%,#2a2a2e 75%,#111 100%)}
.hero h1{position:absolute;left:143px;top:225px;color:#fff;font-size:39px;line-height:50px;font-weight:700}
.hero p{position:absolute;left:145px;top:343px;width:500px;color:#fff;font-size:11.5px;line-height:25px;font-weight:500}
.hero-btn{left:145px;top:419px;width:175px;height:44px}
.mark{position:absolute;width:42px;height:42px;border-radius:50%;background:var(--green)}
.slider-nav{position:absolute;left:68px;top:258px;color:#fff;font-size:11px}
.ribbon{position:absolute;left:-30px;top:688px;width:1280px;height:58px;background:var(--green);transform:rotate(-2.3deg);display:flex;align-items:center;gap:48px;color:#fff;font-family:"Epilogue",sans-serif;font-weight:700;font-size:16px;white-space:nowrap}
.ribbon-back{position:absolute;left:-30px;top:708px;width:1280px;height:48px;background:var(--green-dark);transform:rotate(-1.4deg)}

/* programs */
.section-title{position:absolute;left:0;width:1200px;text-align:center;font-family:"Epilogue",sans-serif;font-weight:600;font-size:24px}
.card-img{position:absolute;top:873px;height:389px}
.tag{position:absolute;bottom:10px;left:0;background:var(--green);color:#fff;font-size:12px;font-weight:500;padding:5px 20px;clip-path:polygon(0 0,100% 0,88% 100%,0 100%)}
.card-cap{position:absolute;top:1283px;font-family:"Epilogue",sans-serif;font-weight:600;font-size:18px}

/* explore */
.explore{top:1342px;left:0;width:1200px;height:535px;background:linear-gradient(90deg,#d8d2c8 0%,#b9b3aa 40%,#5e6e6e 65%,#8a8780 100%)}
.explore h2{position:absolute;left:143px;top:190px;color:#fff;font-size:39px;font-weight:700}
.explore p{position:absolute;left:145px;top:256px;width:460px;color:#fff;font-size:11.5px;line-height:25px}
.explore-btn{left:145px;top:330px;width:190px;height:44px}

/* founder */
.founder-text{position:absolute;left:647px;top:1984px;width:400px}
.founder-text h3{font-size:24px;font-weight:600;line-height:35px}
.founder-text p{font-size:11.5px;line-height:25px;margin-top:22px}
.dots{position:absolute;left:406px;top:2010px;width:170px;height:75px;background-image:radial-gradient(#c9c9c9 1.3px,transparent 1.6px);background-size:14px 14px}

/* press */
.press{position:absolute;left:145px;top:2525px;width:911px;height:178px;display:grid;grid-template-columns:repeat(4,1fr);grid-template-rows:92px 86px;border-top:1px solid var(--line)}
.press div{display:flex;align-items:center;justify-content:center;font-family:"Epilogue",sans-serif;font-weight:700;font-size:22px;color:#8d8d8d;border-right:1px solid var(--line);border-bottom:1px solid var(--line);white-space:nowrap}
.press div:nth-child(4n){border-right:none}
.press .active{box-shadow:0 4px 16px rgba(0,0,0,.12);background:#fff}

/* testimonials */
.stories{top:2762px;left:0;width:1200px;height:455px;background:var(--green)}
.t-card{position:absolute;top:141px;height:210px;background:#fff;display:flex}
.t-photo{width:173px;height:100%}
.t-body{padding:22px 24px}
.t-body h4{font-family:"Epilogue",sans-serif;font-weight:600;font-size:15px;display:flex;justify-content:space-between;width:236px}
.t-body h4 span{color:var(--green);font-size:22px;line-height:14px}
.t-body p{color:#9a9a9a;font-size:11px;line-height:21.5px;margin-top:22px;width:220px}
.stars{color:#e3b81b;font-size:20px;margin-top:8px;letter-spacing:3px}

/* gallery */
.ig{position:absolute}
.follow{left:523px;top:3665px;width:154px;height:44px;gap:10px;font-size:12px}

/* newsletter */
.news{top:3755px;left:0;width:1200px;height:225px;background:linear-gradient(90deg,#f2f2f2,#ececec)}
.news h2{position:absolute;left:140px;top:53px;font-size:34px;font-weight:600;line-height:48px}
.news p{position:absolute;left:143px;top:160px;font-size:10px}
.email{position:absolute;left:687px;top:57px;width:371px;height:48px;border:1px solid #9a9a9a;display:flex;align-items:center;gap:12px;padding-left:16px;font-size:11px}
.subscribe{position:absolute;left:688px;top:120px;width:214px;height:44px;background:var(--green);color:#fff;font-family:"Epilogue",sans-serif;font-weight:700;font-size:10px;display:flex;align-items:center;justify-content:center}

/* footer */
.footer{top:3980px;left:0;width:1200px;height:324px;background:var(--dark);color:#fff}
.f-links{position:absolute;left:146px;top:162px;display:flex;font-size:11.5px;color:#ddd}
.f-links span{padding:0 22px;border-right:1px solid #555}
.f-links span:first-child{padding-left:0}
.f-links span:last-child{border-right:none}
.socials{position:absolute;left:920px;top:158px;display:flex;gap:14px;font-size:11px;font-weight:600}
.f-col{position:absolute;top:243px;font-size:11px;color:#ddd}
.f-col b{display:block;font-weight:500;color:#777;font-size:11px;text-transform:uppercase;margin-bottom:12px}
</style>
</head>
<body>

<header class="abs nav">
  <div class="brand" style="left:143px;top:25px"><i></i>Kelvora</div>
  <nav class="nav-links"><span>Home</span><span>About us</span><span>Services</span><span>The Journal</span><span>Contact us</span></nav>
  <div class="btn login">
    <svg width="14" height="16" viewBox="0 0 14 16" fill="none" stroke="#fff" stroke-width="1.5"><circle cx="7" cy="5" r="3.5"/><path d="M1 15c0-3.5 2.7-5.5 6-5.5s6 2 6 5.5"/></svg>
    Members Login
  </div>
</header>

<section class="abs hero">
  <div class="fill" role="img" aria-label="Athletic woman in sportswear holding a weight plate in a dark gym" style="left:720px;top:0;width:480px;height:610px;background:radial-gradient(ellipse at 50% 45%,#4a3a33 0%,#2a2521 40%,transparent 72%)"></div>
  <div class="mark" style="left:148px;top:150px"></div>
  <h1>Build Your Perfect Body,<br>and Healthy Growth</h1>
  <p>Think you feel too tired to work out? Think again. Your fatigue may be mental rather than physical. Here’s how to tell and how to coerce yourself into a training</p>
  <div class="btn hero-btn">Get Started Now</div>
  <div class="slider-nav">
    <svg width="14" height="60" viewBox="0 0 14 60"><circle cx="7" cy="7" r="6" fill="none" stroke="#9aae1e" stroke-width="1.5"/><circle cx="7" cy="7" r="2.5" fill="#9aae1e"/><circle cx="7" cy="28" r="3" fill="#fff"/><circle cx="7" cy="46" r="3" fill="#fff"/></svg>
    <div style="width:1px;height:70px;background:#fff;margin:4px 0 0 7px"></div>
    <div style="margin-top:8px">1/3</div>
  </div>
  <svg class="abs" style="left:1080px;top:346px" width="76" height="10"><circle cx="5" cy="5" r="3" fill="#fff"/><circle cx="25" cy="5" r="3" fill="#fff"/><circle cx="45" cy="5" r="3" fill="#fff"/><circle cx="67" cy="3" r="3" fill="#fff"/></svg>
  <svg class="abs" style="left:628px;top:556px" width="22" height="26"><rect x="1" y="1" width="20" height="24" rx="10" fill="none" stroke="#9aae1e" stroke-width="1.5"/><rect x="10" y="7" width="2" height="6" fill="#9aae1e"/></svg>
</section>
<div class="ribbon-back"></div>
<div class="ribbon">
  <span>PROGRAM</span><span>✸</span><span>DIET COACHING</span><span>✸</span><span>IN-PERSON COACHING</span><span>✸</span><span>REMOTE COACHING</span><span>✸</span><span>BEST PROFESSIONAL COACH</span>
</div>

<h2 class="section-title" style="top:806px">Special Training Programs</h2>
<div class="card-img" role="img" aria-label="Smiling woman with a green smoothie beside fresh fruit and vegetables" style="left:33px;width:361px;background:linear-gradient(135deg,#5b3f26,#c79a5e 50%,#6f8f3a)"><span class="tag">Nutrition</span></div>
<div class="card-img" role="img" aria-label="Trainer guiding a woman lifting red dumbbells in a gym" style="left:418px;width:361px;background:linear-gradient(135deg,#2a2a2a,#6b6b6b 55%,#3a3a3a)"><span class="tag">Workouts</span></div>
<div class="card-img" role="img" aria-label="Woman on a yoga mat following an online class on a laptop" style="left:804px;width:359px;background:linear-gradient(135deg,#e8e8e8,#8aa6c4 55%,#4f4a45)"><span class="tag">Online</span></div>
<div class="card-cap" style="left:35px">Diet Coaching</div>
<div class="card-cap" style="left:418px">In-Person Coaching</div>
<div class="card-cap" style="left:805px;top:1285px">Remote Coaching</div>

<section class="abs explore" role="img" aria-label="Woman doing leg raises on a mat in a bright living room">
  <div class="mark" style="left:148px;top:118px"></div>
  <h2>Explore The Kelvora Fitness</h2>
  <p>Nulla in eget tortor morbi enim maecenas aenean viverra. Sodales suscipit nunc elit arcu, pulvinar. Vestibulum enim eget vulputate.</p>
  <div class="btn explore-btn">Know More About Us</div>
  <svg class="abs" style="left:932px;top:194px" width="112" height="112" viewBox="0 0 112 112">
    <defs><path id="ring" d="M56,56 m-42,0 a42,42 0 1,1 84,0 a42,42 0 1,1 -84,0"/></defs>
    <text font-family="Poppins,sans-serif" font-size="9" fill="#fff" letter-spacing="4"><textPath href="#ring">PLAY OVER FITNESS · TRAINING ·</textPath></text>
    <circle cx="56" cy="56" r="26" fill="#9aae1e"/>
    <path d="M50 45 L66 56 L50 67 Z" fill="#fff"/>
  </svg>
</section>

<div class="fill" role="img" aria-label="Woman in pink sports top training on a treadmill" style="left:139px;top:1932px;width:267px;height:393px;background:linear-gradient(160deg,#3c4a5e,#8a7d88 50%,#5a3f8a)"></div>
<div class="dots"></div>
<div class="fill" role="img" aria-label="Woman holding red weight plates" style="left:344px;top:2085px;width:232px;height:280px;background:linear-gradient(160deg,#9a9a9a,#cfcfcf 50%,#a23a3a)"></div>
<div class="founder-text">
  <h3>The Kelvora founder<br>Meet Marisol.</h3>
  <p>My life goal is to remind the world that we all have one life to live, and together we should live it to the fullest. I believe that what connects us most is the power of sweat, and physically working through things as a team.</p>
  <p style="margin-top:16px">It is from this evaluative process that we can truly action our philosophy to nurture every person’s current ability whilst guiding them towards.</p>
</div>
<div class="btn" style="left:641px;top:2298px;width:154px;height:44px">More Details</div>

<h2 class="section-title" style="top:2452px">As Seen In</h2>
<div class="press">
  <div>Pulsewell Review</div><div>Mervane</div><div class="active">Quillory</div><div>The Lanternpost</div>
  <div>The Halvard</div><div>Corvessa</div><div>Brindle Courier</div><div>Lustrelle</div>
</div>

<section class="abs stories">
  <h2 class="section-title" style="top:60px;color:#fff">Get Inspired By Success Stories</h2>
  <div class="t-card" style="left:145px;width:431px">
    <div class="t-photo" role="img" aria-label="Smiling woman in a blue sports jacket" style="background:linear-gradient(160deg,#c8d8c8,#3a6aa8)"></div>
    <div class="t-body"><h4>Lorena Ashby<span>❞</span></h4><p>Curabitur sed eros posuere, dictum tortor a, tempor lectus. Morbi vehicul est nunc. In dictum sagittis enim. Nunc eleifend ornare conse quat.</p><div class="stars">★★★★★</div></div>
  </div>
  <div class="t-card" style="left:623px;width:433px">
    <div class="t-photo" role="img" aria-label="Woman jumping on an orange background" style="background:linear-gradient(160deg,#f3a21c,#e07e0e)"></div>
    <div class="t-body"><h4>Bianca Moray<span>❞</span></h4><p>Curabitur sed eros posuere, dictum tortor a, tempor lectus. Morbi vehicul est nunc. In dictum sagittis enim. Nunc eleifend ornare conse quat.</p><div class="stars">★★★★☆</div></div>
  </div>
  <div class="t-card" style="left:1103px;width:97px"><div class="t-photo" role="img" aria-label="Woman running on a light background" style="width:97px;background:linear-gradient(160deg,#e8eef4,#b8c8dc)"></div></div>
  <svg class="abs" style="left:128px;top:234px" width="28" height="28"><circle cx="14" cy="14" r="13" fill="#fff"/><path d="M16 9 L11 14 L16 19" fill="none" stroke="#333" stroke-width="1.6"/></svg>
  <svg class="abs" style="left:148px;top:381px" width="130" height="4"><rect width="32" height="4" fill="#5d6810"/><rect x="38" width="26" height="4" fill="#a4b33a"/><rect x="70" width="26" height="4" fill="#a4b33a"/><rect x="102" width="26" height="4" fill="#a4b33a"/></svg>
</section>

<h2 class="section-title" style="top:3258px">We're on Framely Give us a follow</h2>
<div class="ig" role="img" aria-label="Two women in sports tops posing together" style="left:35px;top:3389px;width:167px;height:199px;background:linear-gradient(160deg,#d8d8d8,#8a8aa8)"></div>
<div class="ig" role="img" aria-label="Two women lifting dumbbells in a gym" style="left:239px;top:3344px;width:241px;height:286px;background:linear-gradient(160deg,#cfcfcf,#a08a90)"></div>
<div class="ig" role="img" aria-label="Woman stretching on a mat in a studio" style="left:515px;top:3389px;width:168px;height:199px;background:linear-gradient(160deg,#bfbfbf,#5a5a62)"></div>
<div class="ig" role="img" aria-label="Woman training, shown with a green overlay" style="left:720px;top:3344px;width:242px;height:286px;background:rgba(140,155,29,.9)">
  <div class="abs" style="left:12px;top:12px;width:22px;height:22px;border:2px solid #fff;border-radius:6px"></div>
  <div class="abs" style="left:48px;top:140px;color:#fff;font-size:13px">♥ 125 &nbsp;&nbsp;&nbsp;&nbsp; ● 60</div>
</div>
<div class="ig" role="img" aria-label="Older woman exercising with small dumbbells" style="left:994px;top:3389px;width:169px;height:199px;background:linear-gradient(160deg,#d0d0d0,#6a6a72)"></div>
<div class="btn follow"><span style="width:16px;height:16px;border:1.5px solid #fff;border-radius:50%;display:block"></span>Follow Us</div>

<section class="abs news">
  <div class="fill" role="img" aria-label="Woman with headphones holding a pink yoga mat" style="left:486px;top:10px;width:180px;height:215px;background:linear-gradient(180deg,#e6e3e3 0%,#d7a8b9 45%,#6f6a6c 100%)"></div>
  <h2>Subscribe To<br>Our Newsletter</h2>
  <p>Subscribe to our mailing list for news, updates and exclusive offers!</p>
  <div class="email"><svg width="16" height="12"><rect x=".5" y=".5" width="15" height="11" fill="none" stroke="#333"/><path d="M1 1 L8 7 L15 1" fill="none" stroke="#333"/></svg>Enter Your Email Address</div>
  <div class="subscribe">SUBSCRIBE NOW</div>
</section>

<footer class="abs footer">
  <div class="brand" style="left:528px;top:46px;color:#fff;font-size:32px"><i></i>Kelvora</div>
  <div class="f-links"><span>Home</span><span>About us</span><span>Services</span><span>The Journal</span><span>Contact us</span><span>Members Login</span><span>Terms &amp; Conditions</span></div>
  <div class="socials"><span>Pixo</span><span>Chirpo</span><span>Framely</span></div>
  <div class="f-col" style="left:146px"><b>Address</b>52 W Alder Rd, Fairhaven, OR 97411, USA</div>
  <div class="f-col" style="left:446px"><b>Phone Number</b>1-555-010-4417</div>
  <div class="f-col" style="left:665px"><b>Email Address</b>hello@kelvora.com</div>
  <div class="f-col" style="left:900px;font-size:9px;color:#888;line-height:18px">©Copyright 2023 <span style="color:#ddd">KELVORA.COM</span><br>All Rights Reserved</div>
</footer>

</body>
</html>
```